STEM business card project for a STEM teacher

I need a business card that is colourful, alive and different to describe my enthusiasm and passion for STEM (Science, Technology, Engineering and Mathematics) teaching
I would like to use specific graphics on the rear of the card. An example of the is can be seen here

https://www.pixelmarsh.example.au/find?q=stem+logo&safe=strict&ref=QX7PLM_enAU481AU481&hl=en-GB&mode=insv&src=menu&tab=img&sa=X&id=0bhVMtR4-EJpwLqXBmYcNdsFgKoRtZwaQ_BVCTHkA&w=1024&h=653#pic=KTMVp552rQ7s_WN:

https://www.pixelmarsh.example.au/find?q=stem+logo&safe=strict&ref=QX7PLM_enAU481AU481&hl=en-GB&mode=insv&src=menu&tab=img&sa=X&id=0bhVMtR4-EJpwLqXBmYcNdsFgKoRtZwaQ_BVCTHkA&w=1024&h=653#pic=UB9ttwKmqeDvaX:

https://www.pixelmarsh.example.au/find?q=stem+logo&safe=strict&ref=QX7PLM_enAU481AU481&hl=en-GB&mode=insv&src=menu&tab=img&sa=X&id=0bhVMtR4-EJpwLqXBmYcNdsFgKoRtZwaQ_BVCTHkA&w=1024&h=653#pic=dwjbXa3ok8r7z-Q:

Industry/Entity Type

Business

Contact Information for Business Card

Owen Brackley
STEM Teacher
Larchmoor College
0455 918 306

Requirements
Must have
• Something that reflects the exciting and changing nature of STEM education
• Eduction is about enabling students to see what they can do and to let them achieve their full potential
• I m absolutely passionate about letting kids enjoy themselves and see how they can use STEM to positively change their world

```html
<!DOCTYPE html>
<html lang="en">
<head>
<meta charset="utf-8">
<title>Owen Brackley – STEM Teacher Business Card</title>
<link rel="stylesheet" href="https://fonts.googleapis.com/css2?family=Cinzel:wght@400&family=Cormorant+Garamond:wght@500&family=Open+Sans:wght@400&display=swap">
<style>
  :root {
    --page: #2a2a2a;
    --card-dark: #1d1d1d;
    --card-light: #ffffff;
    --ink-light: #ffffff;
    --ink-dark: #333333;
    --rule: #555555;
    --stem-red: #8a2a24;
    --stem-yellow: #8a7a1e;
    --stem-blue: #1f4f7a;
    --stem-green: #3f6a2a;
  }
  * { margin: 0; padding: 0; box-sizing: border-box; }
  html, body {
    width: 1200px; height: 900px; overflow: hidden;
    background: var(--page);
  }
  .sheet {
    position: relative; width: 1200px; height: 900px;
  }
  .card {
    position: absolute; left: 280px; width: 640px; height: 366px;
    overflow: hidden;
    box-shadow: 0 12px 30px rgba(0,0,0,.45);
  }
  .card--front { top: 64px; background: var(--card-dark); }
  .card--back  { top: 470px; background: var(--card-light); }

  .front__art {
    position: absolute; inset: 0;
    background:
      linear-gradient(90deg,
        var(--stem-red) 0%, var(--stem-red) 18%,
        var(--stem-yellow) 30%, var(--stem-yellow) 45%,
        var(--stem-blue) 58%, var(--stem-blue) 72%,
        var(--stem-green) 84%, var(--stem-green) 100%);
    opacity: .35;
  }
  .front__title {
    position: absolute; left: 40px; top: 92px;
    font-family: "Cormorant Garamond", serif; font-weight: 500;
    font-size: 72px; letter-spacing: 3px; color: var(--ink-light);
    line-height: 1;
  }
  .front__quote {
    position: absolute; left: 28px; top: 196px; right: 24px;
    font-family: "Open Sans", sans-serif; font-size: 13.5px;
    line-height: 1.25; color: var(--ink-light);
  }
  .front__quote span { display: block; }
  .front__quote span:nth-child(2) { padding-left: 0; }
  .front__quote span:last-child { padding-top: 2px; }

  .back__name {
    position: absolute; left: 50px; top: 196px;
    font-family: "Cinzel", serif; font-size: 30px; color: var(--ink-dark);
    letter-spacing: 1px; line-height: 1;
  }
  .back__role {
    position: absolute; left: 52px; top: 232px;
    font-family: "Cinzel", serif; font-size: 14px; color: var(--ink-dark);
  }
  .back__rule {
    position: absolute; left: 48px; top: 260px; width: 520px; height: 1px;
    background: var(--rule);
  }
  .back__school {
    position: absolute; left: 48px; top: 276px;
    font-family: "Cinzel", serif; font-size: 18px; color: var(--ink-dark);
  }
  .back__phone {
    position: absolute; left: 48px; top: 302px;
    font-family: "Cinzel", serif; font-size: 17px; color: var(--ink-dark);
  }
</style>
</head>
<body>
<main class="sheet">
  <section class="card card--front">
    <div class="front__art" role="img" aria-label="Colourful STEM lettering illustration with atom, laptop circuit, gear, ruler and apple icons"></div>
    <h1 class="front__title">STEM</h1>
    <p class="front__quote">
      <span>Eduction is about enabling students to see</span>
      <span>What they can do and to let them achieve their full potential</span>
      <span>I m absolutely passionate about letting kids enjoy</span>
      <span>Themselves and see how they can use STEM to positively change their world</span>
    </p>
  </section>

  <section class="card card--back">
    <h2 class="back__name">OWEN BRACKLEY</h2>
    <p class="back__role">STEM TEACHER</p>
    <div class="back__rule"></div>
    <p class="back__school">LARCHMOOR COLLEGE</p>
    <p class="back__phone">P : 0455 918 306</p>
  </section>
</main>
</body>
</html>
```